This is for a poster that will be hanging in the window of a Men's Suit Store in the mall:
Size 4 feet wide by 6 feet high
Main point is: A sale on "Suits" or "Men's Suits" at 40%-60% off ( the 40%-60% off should be the focal point)
Some words that can be used are "Sale" or "Clearance Sale"
Some key words that can be used to make it urgent are "limited time offer" or something similar.
You can get creative, the point is for the customer to want to come into the store and buy a suit right away.
You may use a graphic (picture of a man in a suit). It is not necessary but if it looks good you can use it. (If you do use a picture, it should be of a modern fit or slim fit suit)
Sorry, the initial brief somehow got deleted from the project. Please see the updated brief.
Thanks
Reason: Project was closed for some reason, extended to give enough time to complete
Target Market(s)
Mostly Men ages 35-55
Industry/Entity Type
Store
Colors
Designer to choose colors to be used in the design.

```html
<!DOCTYPE html>
<html lang="en">
<head>
<meta charset="utf-8">
<title>Men's Suits Sale Poster</title>
<link href="https://fonts.googleapis.com/css2?family=Roboto+Condensed:wght@700&display=swap" rel="stylesheet">
<style>
  :root {
    --frame: #000000;
    --sky: #b3dcf1;
    --sky-deep: #a4d2ea;
    --band: #131619;
    --ink: #0d0d0d;
    --paper: #ffffff;
    --suit-light: #4a2a36;
    --suit-dark: #1c1116;
  }
  * { margin: 0; padding: 0; box-sizing: border-box; }
  html, body { width: 800px; height: 1200px; overflow: hidden; background: var(--frame); }
  .poster {
    position: relative;
    width: 800px;
    height: 1200px;
    background: var(--frame);
    font-family: "Roboto Condensed", "Arial Narrow", sans-serif;
    font-weight: 700;
    overflow: hidden;
  }
  .poster__panel {
    position: absolute;
    left: 26px; top: 26px;
    width: 748px; height: 1147px;
    background: radial-gradient(ellipse at 40% 55%, var(--sky) 0%, var(--sky-deep) 100%);
  }
  .poster__band {
    position: absolute;
    left: 26px; top: 488px;
    width: 748px; height: 222px;
    background: var(--band);
  }
  .poster__model {
    position: absolute;
    left: 515px; top: 26px;
    width: 259px; height: 1112px;
    background: linear-gradient(180deg, var(--suit-light) 0%, var(--suit-dark) 45%, var(--suit-light) 80%, var(--suit-dark) 100%);
    opacity: 0.92;
  }
  .headline {
    position: absolute;
    left: 72px; top: 58px;
    color: var(--ink);
    text-transform: uppercase;
  }
  .headline__sale {
    display: block;
    font-size: 204px;
    line-height: 0.85;
    letter-spacing: -2px;
  }
  .headline__category {
    display: block;
    margin-top: 16px;
    font-size: 60px;
    line-height: 1;
    letter-spacing: 7px;
  }
  .offer {
    position: absolute;
    left: 58px; top: 518px;
    color: var(--paper);
    font-size: 136px;
    line-height: 1;
    letter-spacing: 4px;
    white-space: nowrap;
  }
  .brand {
    position: absolute;
    left: 60px; top: 1104px;
    display: flex;
    align-items: center;
    gap: 14px;
    color: var(--ink);
    font-size: 40px;
    line-height: 1;
    letter-spacing: 3px;
    text-transform: uppercase;
  }
  .brand__square {
    width: 26px; height: 26px;
    background: var(--ink);
  }
</style>
</head>
<body>
  <main class="poster">
    <div class="poster__panel"></div>
    <div class="poster__band"></div>
    <div class="poster__model" role="img" aria-label="Photo of a man in a slim-fit plum suit with gingham shirt and black shoes, cropped at the shoulders"></div>
    <h1 class="headline">
      <span class="headline__sale">Sale</span>
      <span class="headline__category">Men’s Suits</span>
    </h1>
    <p class="offer">40-60% OFF</p>
    <div class="brand">
      <span class="brand__square"></span>
      <span class="brand__name">Mercer &amp; Co.</span>
    </div>
  </main>
</body>
</html>
```